Open Sky Living newsletter - Mail Chimp

Open Sky Living - Empowering Life Coach needs Mail Chimp Newsletter Template. This is a newsletter I will send out monthly to current clients and prospective clients to offer (hopefully) inspiring and uplifting content AND to give info and dates of my upcoming workshops and retreats.

I have attached a word document with all of the different sections of the mail chimp template I would like to have - and hte actual content for the first newsletter.

I'd like to look uplifting, fun, inspiring.

I also need it to be easy for me to use to update in the future :)

Target Market(s)

Women - moms

Industry/Entity Type

Life Coaching

Requirements
Nice to have
• Color theme to match my "Open Sky Living" logo

```html
<!DOCTYPE html>
<html lang="en">
<head>
<meta charset="utf-8">
<title>Open Sky Living Newsletter</title>
<link rel="stylesheet" href="https://fonts.googleapis.com/css2?family=Arimo:ital,wght@0,400;0,700;1,400&family=Chewy&display=swap">
<style>
  :root {
    --ink: #1f1f1f;
    --sky-blue: #1c8fc9;
    --sky-blue-deep: #156fa3;
    --sand: #dcb57a;
    --rose: #d6195b;
    --aqua: #27a9e1;
    --purple: #5b2a86;
    --leaf: #7cc242;
    --orange: #f59a12;
    --mist: #ebebeb;
    --shadow-grey: #e3e3e3;
    --white: #ffffff;
  }
  * { box-sizing: border-box; margin: 0; padding: 0; }
  html, body { width: 1200px; height: 3704px; overflow: hidden; background: var(--white); }
  body { font-family: "Arimo", Arial, sans-serif; color: var(--ink); font-size: 21px; line-height: 32px; }
  .newsletter { position: relative; width: 1200px; height: 3704px; overflow: hidden; }
  .block { position: absolute; left: 54px; width: 1096px; }
  .block p { margin-bottom: 30px; }
  .block p:last-child { margin-bottom: 0; }

  /* header */
  .masthead { position: absolute; left: 0; top: 0; width: 1200px; height: 604px; background: linear-gradient(135deg, #c9862a, #e2a94a); }
  .masthead-photo { position: absolute; right: 0; top: 0; width: 830px; height: 604px;
    background: radial-gradient(circle at 48% 62%, #fff4d6 0%, #f3cf7d 22%, #c98e3f 55%, #7b5a3a 100%); }
  .masthead-frame { position: absolute; left: 0; top: 110px; width: 640px; height: 494px; background: var(--sand); opacity: .85; }
  .masthead-panel { position: absolute; left: 0; top: 150px; width: 580px; height: 454px; border-radius: 0 48px 0 0;
    background: linear-gradient(160deg, var(--aqua), var(--sky-blue-deep)); display: flex; align-items: center; justify-content: center; gap: 18px; }
  .brand-dot { width: 34px; height: 34px; border-radius: 50%; background: var(--white); }
  .brand-name { font-weight: 700; color: var(--white); font-size: 54px; line-height: 1.1; }

  .rule { position: absolute; left: 54px; top: 1168px; width: 1093px; height: 5px; background: var(--purple); }

  .section-title { position: absolute; left: 0; top: 1232px; width: 1200px; text-align: center; }
  .section-title h2 { font-family: "Chewy", "Comic Sans MS", cursive; font-weight: 400; color: var(--rose); font-size: 44px; letter-spacing: 1px; line-height: 50px; }
  .section-title svg { display: block; margin: -6px auto 0; }

  .subhead { font-weight: 700; }
  .checklist { list-style: none; margin: 14px 0 14px; }
  .checklist li { position: relative; padding-left: 42px; }
  .checklist li::before { content: "✓"; position: absolute; left: 4px; }

  /* reflection cards */
  .card { position: absolute; top: 1769px; width: 440px; height: 345px; }
  .card-shadow { position: absolute; left: 22px; top: 22px; width: 440px; height: 345px; background: var(--shadow-grey); }
  .card-frame { position: absolute; inset: 0; border: 7px solid; background: var(--white); padding: 56px 30px 20px 38px; font-size: 19px; line-height: 24px; }
  .card-frame h3 { font-size: 19px; font-weight: 700; margin-bottom: 22px; }
  .card-frame em { display: block; }
  .card-pink { left: 106px; }
  .card-pink .card-frame { border-color: var(--rose); }
  .card-blue { left: 636px; }
  .card-blue .card-frame { border-color: var(--aqua); }

  .band { position: absolute; left: 0; top: 2193px; width: 1200px; height: 377px; background: var(--mist); }
  .band-text { position: absolute; left: 54px; top: 106px; width: 520px; font-weight: 700; font-size: 21px; line-height: 30px; }
  .band-text p { margin-bottom: 30px; }
  .quote-art { position: absolute; top: 25px; height: 327px; }
  .quote-one { left: 599px; width: 214px; background: linear-gradient(180deg, #2d3f5c, #0f1626); }
  .quote-two { left: 813px; width: 335px; background: linear-gradient(180deg, #e8e9ec, #b9c2b4); }

  .heading-link { font-weight: 700; text-decoration: underline; }

  .partner { position: absolute; left: 812px; top: 2978px; width: 340px; height: 60px; display: flex; align-items: center; gap: 12px; }
  .partner-dot { width: 30px; height: 30px; border-radius: 50%; background: var(--sky-blue); }
  .partner-name { color: var(--sky-blue-deep); font-size: 26px; }
  .partner-gap { float: right; width: 370px; height: 92px; }

  .date-pill { position: absolute; left: 54px; top: 3230px; width: 630px; height: 62px; border-radius: 14px; background: var(--rose);
    color: var(--white); font-weight: 700; font-size: 32px; display: flex; align-items: center; justify-content: center; }
  .time-pill { position: absolute; left: 212px; top: 3317px; width: 315px; height: 60px; border-radius: 14px; background: var(--orange);
    color: var(--white); font-weight: 700; font-size: 32px; display: flex; align-items: center; justify-content: center; }
  .connector { position: absolute; left: 0; top: 0; }
  .venue { width: 680px; }
  .venue a { color: var(--rose); font-weight: 700; }
  .quote-portrait { position: absolute; left: 769px; top: 3186px; width: 379px; height: 382px; background: linear-gradient(135deg, #5b5b5b, #1d1d1d); border: 6px solid #111; }

  .footer { position: absolute; left: 54px; top: 3610px; width: 1092px; font-size: 16px; line-height: 22px; }
  .footer a { color: var(--sky-blue); font-weight: 700; text-decoration: none; }
</style>
</head>
<body>
<main class="newsletter">

  <header class="masthead">
    <div class="masthead-frame"></div>
    <div class="masthead-photo" role="img" aria-label="Photo of two hands forming a heart shape against a glowing sunset sky"></div>
    <div class="masthead-panel">
      <span class="brand-dot"></span>
      <span class="brand-name">Open Sky Living</span>
    </div>
  </header>

  <section class="block" style="top:655px;">
    <p>Hello Friends!!</p>
    <p>I am excited to (hopefully) add a little love to your in-box with this newsletter. I love connecting with moms and helping them find tools to make their lives happier, more intentional, and more fun and this is a new way to do that!</p>
    <p>If you don’t know me well, I am a certified Boundless Horizons Trainer and I lead coaching groups for moms. My BH workshops and Thriving Moms Coaching Group have the goal of fostering connections between amazing women and empowering moms with tools to build lives they are enthusiastic about living, on purpose – and that will be the goal of this newsletter, as well!</p>
    <p>I hope you find something useful and helpful and enjoy receiving this info (and if not, feel free to unsubscribe and my feelings will not be hurt!)!</p>
    <p>With love,</p>
    <p>Dana</p>
  </section>

  <div class="rule"></div>

  <div class="section-title">
    <h2>OPEN SKY LIVING TIPS &amp; TOOLS:</h2>
    <svg width="540" height="18" viewBox="0 0 540 18" aria-hidden="true">
      <path d="M2 0 V14 H538 V0" fill="none" stroke="var(--leaf)" stroke-width="3"/>
    </svg>
  </div>

  <section class="block" style="top:1358px;">
    <p style="margin-bottom:0;" class="subhead">Building Happiness</p>
    <p>I firmly believe that thinking about your happiness is important and that happiness itself is a worthwhile goal! If you think about all the things you focus on in your life and all the goals you set for yourself, all of those things are leading you toward feeling happier. Happiness, in the end, is the ultimate goal.</p>
    <p style="margin-bottom:0;">Of course, what makes each person happy is totally different – and that’s awesome and one part of what makes life fun and exciting! Many happiness experts and authors note that the key ingredients in our lives that will make us happier are pursuing 2 categories:</p>
    <ul class="checklist">
      <li>things that bring us pleasure (positive emotions) <em><u>and</u></em></li>
      <li>things that bring us meaning &amp; fulfillment</li>
    </ul>
    <p>Give yourself a minute to think about (it’s extra powerful if you write it down!) what makes YOU happy.</p>
  </section>

  <div class="card card-pink">
    <div class="card-shadow"></div>
    <div class="card-frame">
      <h3>What are things that make you feel happy / provide you with pleasure (little and big things!)?</h3>
      <em>For me: joking &amp; laughing with my kids &amp; husband, petting with my dog, sitting with a soft blanket and a book, my first sip of coffee in the morning, walking in nature, travelling, scuba diving, exercise classes, making my friends laugh.</em>
    </div>
  </div>

  <div class="card card-blue">
    <div class="card-shadow"></div>
    <div class="card-frame">
      <h3>What are things that are meaningful to you / make you feel fulfilled (little and big things!)?</h3>
      <em>For me: teaching Boundless Horizons workshops, spending quality time with my family, making gratitude lists, volunteering, leading moms’ coaching groups, making my kids breakfast.</em>
    </div>
  </div>

  <section class="band">
    <div class="band-text">
      <p>How could you add more of those things that bring you happiness to your days?</p>
      <p>Try to add 1 or 2 of those things per week and see how your happiness increases! You are worth it!</p>
    </div>
    <div class="quote-art quote-one" role="img" aria-label="Quote graphic on a dark evening sky: happiness is something you design for the present"></div>
    <div class="quote-art quote-two" role="img" aria-label="Quote graphic over a soft misty landscape: happiness is found in the simplest of things"></div>
  </section>

  <section class="block" style="top:2636px;">
    <p><span class="heading-link">Empowering Books:</span><br>I love to read uplifting, inspiring material. Each newsletter, I’ll suggest a few books that I’ve enjoyed!</p>
    <p>The Joy Journal by Marian Hale</p>
    <p style="margin-bottom:14px;">You Are Unstoppable. How to Quiet Your Doubts and Start Living a Brilliant Life” by Lena Corvo</p>
    <p style="margin-bottom:16px;"><span class="heading-link">Upcoming Events:</span><br>I lead a Boundless Horizons Workshop 2-3 times per year. The next one is coming up in September / October. More details to come – but here is a little info...</p>
    <p class="subhead" style="margin-bottom:30px;">Moms - Back to School, Back to You!</p>
    <p style="margin-bottom:18px;"><span class="partner-gap"></span>In September, the kids will be going back to school and you can spend time focusing on YOU. Let this be the year where you take time to focus on yourself so that you can feel amazing, focused, fulfilled, purposeful, and happier!  Take the time to learn some simple tools to help you live a life you love, deliberately, instead of just juggling what comes at you and juggling your to-do list.  In this workshop, you will be empowered to build a life you love.</p>
    <p class="subhead">Dates: 3 morning workshop</p>
  </section>

  <div class="partner">
    <span class="partner-dot"></span>
    <span class="partner-name">Boundless Horizons</span>
  </div>

  <div class="date-pill">September 27, October 4, October 11</div>
  <svg class="connector" width="1200" height="3704" aria-hidden="true">
    <path d="M240 3292 V3317 M368 3292 V3317 M496 3292 V3317" stroke="#9a9a9a" stroke-width="3"/>
  </svg>
  <div class="time-pill">9:30 – 12:30</div>

  <section class="block venue" style="top:3404px;">
    <p>Dana’s home in Cedar Ridge<br>Interested? Email me: <a href="mailto:dana@openskyliving.example">dana@openskyliving.example</a></p>
    <p>Enjoy the rest of Summer Break! Savor each amazing day! How can you add a little more HAPPY to your August?? Make the choice and do it!</p>
  </section>

  <div class="quote-portrait" role="img" aria-label="Black and white quote graphic about choosing happiness as a life goal"></div>

  <footer class="footer">
    This email is sent by Brightline Mail Ltd on behalf of CLIENT NAME. We only send emails that we feel are relevant to you. You can unsubscribe from future emails from this client by clicking <a href="#">here.</a>
  </footer>
</main>
</body>
</html>
```